Business Card Design Project

Build kick ass business card.
Updates

I just uploaded the Veruxo Logo in AI format, for those that were asking. It's looking real good and we'll be reviewing the designs soon. Thanks. 

Target Market(s)

Businesses in many verticals. Focusing on information security.

Veruxo, LLC
Darren Colby
Principal Security Consultant
Mobile: +1-480-555-0137
Email: Darren.Colby@Veruxo.example
Web: www.veruxo.example

Industry/Entity Type

Business

Requirements
Must have
• Design must look high-end, hi-tech stylish and minimalist

Be different – one that stands out from thousands of others

Does not have to be traditional rectangle

Would like logo integrated

```html
<!DOCTYPE html>
<html lang="en">
<head>
<meta charset="utf-8">
<title>Veruxo, LLC — Darren Colby</title>
<link rel="stylesheet" href="https://fonts.googleapis.com/css2?family=Open+Sans:wght@400;600;700&display=swap">
<style>
  :root {
    --tab-grey: #8a8a8a;
    --band-grey: #8e8e8e;
    --stripe-sky: #29abe2;
    --stripe-blue: #0072bc;
    --stripe-slate: #666666;
    --ink: #1a1a1a;
    --card-edge: #a0a0a0;
    --paper: #ffffff;
    --marker: #0072bc;
  }
  html, body {
    margin: 0;
    padding: 0;
    width: 1200px;
    height: 639px;
    overflow: hidden;
    background: var(--paper);
    font-family: "Open Sans", Arial, sans-serif;
  }
  .card {
    position: relative;
    width: 1200px;
    height: 639px;
  }
  .company-tab {
    position: absolute;
    left: 419px;
    top: 0;
    width: 362px;
    height: 60px;
    background: var(--tab-grey);
    border-radius: 26px 26px 0 0;
  }
  .company-tab__name {
    position: absolute;
    left: 0;
    right: 0;
    top: 9px;
    text-align: center;
    color: var(--paper);
    font-size: 28px;
    font-weight: 600;
    line-height: 1;
    letter-spacing: 0.5px;
  }
  .card-body {
    position: absolute;
    left: 1px;
    top: 44px;
    width: 1196px;
    height: 592px;
    border: 1px solid var(--card-edge);
    border-top: none;
    border-radius: 44px 44px 2px 2px;
    overflow: hidden;
    background: var(--paper);
  }
  .header-band {
    position: absolute;
    left: 0;
    top: 0;
    width: 100%;
    height: 61px;
    background: var(--band-grey);
  }
  .colour-stripes {
    position: absolute;
    left: 0;
    top: 61px;
    width: 100%;
    height: 25px;
    display: flex;
  }
  .colour-stripes span { display: block; height: 100%; }
  .stripe--sky { width: 402px; background: var(--stripe-sky); }
  .stripe--blue { width: 402px; background: var(--stripe-blue); }
  .stripe--slate { flex: 1; background: var(--stripe-slate); }

  .contact {
    position: absolute;
    left: 436px;
    top: 0;
    color: var(--ink);
    line-height: 1;
  }
  .contact > * { position: absolute; left: 0; white-space: nowrap; margin: 0; }
  .contact__title { top: 156px; font-size: 31px; font-weight: 400; }
  .contact__title strong { font-weight: 700; }
  .contact__title .divider { font-weight: 700; margin: 0 20px 0 22px; }
  .contact__email { top: 209px; font-size: 19px; }
  .contact__phone { top: 252px; font-size: 15px; }
  .contact__phone .label { font-size: 12px; margin-right: 4px; }
  .contact__rule {
    top: 272px;
    width: 369px;
    height: 2px;
    background: var(--ink);
  }
  .contact__web { top: 286px; font-size: 29px; }

  .brand {
    position: absolute;
    left: 150px;
    top: 436px;
    display: flex;
    align-items: center;
  }
  .brand__marker {
    width: 56px;
    height: 56px;
    border-radius: 50%;
    background: var(--marker);
    margin-right: 24px;
  }
  .brand__name {
    font-size: 56px;
    font-weight: 400;
    color: var(--ink);
    line-height: 1;
  }
</style>
</head>
<body>
  <div class="card">
    <div class="company-tab">
      <div class="company-tab__name">VERUXO, LLC</div>
    </div>
    <div class="card-body">
      <div class="header-band"></div>
      <div class="colour-stripes">
        <span class="stripe--sky"></span>
        <span class="stripe--blue"></span>
        <span class="stripe--slate"></span>
      </div>
    </div>

    <div class="contact">
      <p class="contact__title"><strong>darren colby</strong><span class="divider">\</span>principal security consultant</p>
      <p class="contact__email">Darren.Colby@Veruxo.example</p>
      <p class="contact__phone"><span class="label">PH</span>+1 480 555-0137</p>
      <div class="contact__rule"></div>
      <p class="contact__web">www.veruxo.example</p>
    </div>

    <div class="brand">
      <div class="brand__marker"></div>
      <div class="brand__name">Veruxo</div>
    </div>
  </div>
</body>
</html>
```